Marlowen

I'm looking for business cards with the logo I've attached. I don't have an specific idea in mind and open to anything. All the usual info will be involved. Name, position in company, nr, email, address

```html
<!DOCTYPE html>
<html lang="en">
<head>
<meta charset="utf-8">
<title>Marlowen business cards</title>
<link href="https://fonts.googleapis.com/css2?family=Montserrat:wght@400;500;700;800&display=swap" rel="stylesheet">
<style>
  :root {
    --gold: #ecb13a;
    --navy: #1a2b4c;
    --paper: #ffffff;
    --backdrop: #5d5d61;
    --rule: #4a5670;
  }
  * { margin: 0; padding: 0; box-sizing: border-box; }
  html, body { width: 1200px; height: 1200px; overflow: hidden; }
  body {
    background: var(--backdrop);
    font-family: "Montserrat", sans-serif;
    display: flex;
    flex-direction: column;
    align-items: center;
    justify-content: center;
    gap: 56px;
  }
  .card {
    width: 900px;
    height: 514px;
    border-radius: 30px;
    position: relative;
    overflow: hidden;
  }
  .card--front {
    background: var(--gold);
    display: flex;
    align-items: center;
    justify-content: center;
    gap: 22px;
  }
  .front-mark {
    width: 40px; height: 40px;
    border-radius: 50%;
    background: var(--navy);
  }
  .front-name {
    color: var(--navy);
    font-weight: 800;
    font-size: 64px;
    letter-spacing: 1px;
  }
  .card--back {
    background: var(--paper);
    display: flex;
    align-items: center;
  }
  .brand {
    width: 430px;
    display: flex;
    justify-content: center;
    align-items: center;
    gap: 16px;
  }
  .brand-mark {
    width: 30px; height: 30px;
    border-radius: 50%;
    background: var(--gold);
  }
  .brand-name {
    color: var(--gold);
    font-weight: 800;
    font-size: 58px;
    letter-spacing: 0.5px;
  }
  .divider {
    width: 1.5px;
    height: 260px;
    background: var(--rule);
  }
  .details {
    padding-left: 36px;
    color: var(--navy);
  }
  .person-name {
    font-weight: 800;
    font-size: 30px;
    letter-spacing: 1px;
    text-transform: uppercase;
  }
  .person-role {
    color: var(--gold);
    font-weight: 700;
    font-size: 20px;
    margin-bottom: 22px;
  }
  .address {
    font-size: 17px;
    line-height: 1.4;
    margin-bottom: 12px;
  }
  .contact-list { list-style: none; }
  .contact-list li {
    font-size: 17px;
    line-height: 1.55;
    display: flex;
    align-items: center;
    gap: 8px;
  }
  .contact-list svg { width: 16px; height: 16px; flex: none; }
  .web strong { font-weight: 700; }
</style>
</head>
<body>
  <section class="card card--front">
    <span class="front-mark"></span>
    <span class="front-name">Marlowen</span>
  </section>

  <section class="card card--back">
    <div class="brand">
      <span class="brand-mark"></span>
      <span class="brand-name">Marlowen</span>
    </div>
    <div class="divider"></div>
    <div class="details">
      <h1 class="person-name">Dorian Vale</h1>
      <p class="person-role">Owner</p>
      <p class="address">48/6 Harrowgate Lane,<br>Elm Ridge, Vic 3480, Linz, Austria</p>
      <ul class="contact-list">
        <li>
          <svg viewBox="0 0 24 24" aria-hidden="true"><path fill="var(--gold)" d="M6.6 10.8a15 15 0 0 0 6.6 6.6l2.2-2.2c.3-.3.7-.4 1-.2 1.1.4 2.3.6 3.6.6.6 0 1 .4 1 1V20c0 .6-.4 1-1 1A17 17 0 0 1 3 4c0-.6.4-1 1-1h3.5c.6 0 1 .4 1 1 0 1.3.2 2.5.6 3.6.1.3 0 .7-.2 1z"/></svg>
          (555) 018 4417
        </li>
        <li>
          <svg viewBox="0 0 24 24" aria-hidden="true"><rect x="6" y="2" width="12" height="20" rx="2" fill="none" stroke="var(--gold)" stroke-width="2"/><circle cx="12" cy="18" r="1.2" fill="var(--gold)"/></svg>
          (555) 018 4418
        </li>
        <li>
          <svg viewBox="0 0 24 24" aria-hidden="true"><rect x="2" y="5" width="20" height="14" rx="1.5" fill="var(--gold)"/><path d="M3 6l9 7 9-7" fill="none" stroke="#fff" stroke-width="1.6"/></svg>
          info@marlowendesigns.com
        </li>
        <li class="web">
          <svg viewBox="0 0 24 24" aria-hidden="true"><circle cx="12" cy="12" r="9" fill="none" stroke="var(--gold)" stroke-width="2"/><path d="M3 12h18M12 3c3 3 3 15 0 18M12 3c-3 3-3 15 0 18" fill="none" stroke="var(--gold)" stroke-width="1.5"/></svg>
          <span><strong>marlowendesigns</strong>.com</span>
        </li>
      </ul>
    </div>
  </section>
</body>
</html>
```